New Word Template Design Project

I need this document for death certificate ordering to look like our branding. I will attach the pdf with the information and a sample pdf of our style. I also think that check boxes and x's would be better than yes and no.

2nd page in spanish.

Industry/Entity Type

Funeral

Requirements
Should not have
• Check boxes and red x's or yellow next to the yes, no , or sometimes

```html
<!DOCTYPE html>
<html lang="en">
<head>
<meta charset="utf-8">
<title>Certified Death Certificates – Hollis Crane</title>
<link href="https://fonts.googleapis.com/css2?family=Roboto:wght@400;500;700&display=swap" rel="stylesheet">
<style>
  :root{
    --slate:#4e6e89;
    --gold:#cc9a16;
    --ink:#2b2b2b;
    --row-tint:#f3f7fb;
    --row-line:#d9dee3;
    --tick:#2fb344;
    --cross:#e01b1b;
    --white:#ffffff;
  }
  *{box-sizing:border-box;margin:0;padding:0}
  html,body{width:855px;height:1200px;overflow:hidden;background:var(--white)}
  body{position:relative;font-family:'Roboto',sans-serif;color:var(--ink)}

  .frame-line{position:absolute;border:1px solid var(--slate)}
  .frame-outer{left:21px;top:22px;width:813px;height:1152px}
  .frame-inner{left:25px;top:26px;width:805px;height:1144px}
  .frame-gap{position:absolute;left:312px;top:18px;width:231px;height:12px;background:var(--white)}

  .brand{position:absolute;left:0;top:38px;width:855px;text-align:center;
    font-size:34px;font-weight:500;color:var(--slate);letter-spacing:.5px}

  .intro{position:absolute;left:46px;top:120px;width:763px;font-size:13.7px;
    line-height:20px;text-align:justify}

  .uses{position:absolute;left:46px;top:188px;display:grid;
    grid-template-columns:262px 164px 164px 165px;gap:3px}
  .uses .head{height:30px;background:var(--slate);color:var(--white);font-weight:700;
    font-size:13px;display:flex;align-items:center;padding-left:22px}
  .uses .cell{height:30px;border:1px solid var(--row-line);font-size:11px;
    display:flex;align-items:center;padding-left:22px;gap:4px}
  .uses .tint{background:var(--row-tint)}
  .mark{width:11px;height:11px;flex:none}

  .price-band{position:absolute;left:46px;top:729px;width:764px;height:35px;
    background:var(--gold);color:var(--white);font-weight:700;font-size:15px;
    display:flex;align-items:center;justify-content:center}

  .note{position:absolute;left:46px;width:764px;font-size:13.7px;line-height:20px;text-align:justify}

  .panel{position:absolute;top:1015px;width:373px;height:104px;color:var(--white);padding:13px 18px}
  .panel-order{left:46px;background:var(--slate)}
  .panel-contact{left:436px;background:var(--gold)}
  .panel h2{font-size:13px;font-weight:700;margin-bottom:7px}
  .panel p{font-size:11.5px;line-height:20px;display:flex;align-items:flex-start;gap:7px}
  .box{width:10px;height:10px;background:var(--white);border-radius:2px;margin-top:5px;flex:none}
  .ico{width:10px;height:10px;flex:none;margin-top:5px}

  .closing{position:absolute;left:0;top:1131px;width:855px;text-align:center;font-weight:700;font-size:13px}
</style>
</head>
<body>
<svg width="0" height="0" style="position:absolute">
  <symbol id="tick" viewBox="0 0 12 12">
    <rect x="1" y="2" width="9" height="9" rx="1.5" fill="none" stroke="#2fb344" stroke-width="1.4"/>
    <path d="M3.2 6.2 5.4 8.3 11 2.2" fill="none" stroke="#2fb344" stroke-width="1.8" stroke-linecap="round" stroke-linejoin="round"/>
  </symbol>
  <symbol id="cross" viewBox="0 0 12 12">
    <path d="M2.5 2.5 9.5 9.5M9.5 2.5 2.5 9.5" stroke="#e01b1b" stroke-width="2.4" stroke-linecap="round"/>
  </symbol>
</svg>

<div class="frame-line frame-outer"></div>
<div class="frame-line frame-inner"></div>
<div class="frame-gap"></div>

<div class="brand">Hollis Crane</div>

<p class="intro">Certified death certificates are used to handle legal, financial, and personal matters after a loved one passes. While some institutions require an original, others may only need to view or copy it. In Florida, you can order death certificates with or without the cause of death. Cause of death is confidential and should only be included when necessary.</p>

<div class="uses">
  <div class="head">Use</div><div class="head">Original Needed?</div><div class="head">With Cause?</div><div class="head">Suggested Quantity</div>

  <div class="cell tint">Life Insurance Claims</div><div class="cell tint"><svg class="mark"><use href="#tick"/></svg>Yes</div><div class="cell tint"><svg class="mark"><use href="#tick"/></svg>Yes</div><div class="cell tint">1 per policy</div>
  <div class="cell">Pension or Retirement Benefits</div><div class="cell"><svg class="mark"><use href="#tick"/></svg>Yes</div><div class="cell"><svg class="mark"><use href="#tick"/></svg>Yes</div><div class="cell">1</div>
  <div class="cell tint">Bank Accounts</div><div class="cell tint"><svg class="mark"><use href="#cross"/></svg>Usually Not</div><div class="cell tint"><svg class="mark"><use href="#cross"/></svg>No</div><div class="cell tint">0–1</div>
  <div class="cell">Investment / Brokerage Accounts</div><div class="cell"><svg class="mark"><use href="#tick"/></svg>Sometimes</div><div class="cell"><svg class="mark"><use href="#tick"/></svg>Sometimes</div><div class="cell">1–2</div>
  <div class="cell tint">Vehicle Title Transfer (DMV)</div><div class="cell tint"><svg class="mark"><use href="#tick"/></svg>Yes</div><div class="cell tint"><svg class="mark"><use href="#cross"/></svg>No</div><div class="cell tint">2</div>
  <div class="cell">Property / Real Estate Transfers</div><div class="cell"><svg class="mark"><use href="#tick"/></svg>Yes</div><div class="cell"><svg class="mark"><use href="#cross"/></svg>No</div><div class="cell">1 per property</div>
  <div class="cell tint">Probate / Court Matters</div><div class="cell tint"><svg class="mark"><use href="#tick"/></svg>Yes</div><div class="cell tint"><svg class="mark"><use href="#tick"/></svg>Often</div><div class="cell tint">1–2</div>
  <div class="cell">Social Security / Government Benefits</div><div class="cell"><svg class="mark"><use href="#cross"/></svg>No</div><div class="cell"><svg class="mark"><use href="#cross"/></svg>No</div><div class="cell">0</div>
  <div class="cell tint">Passport Cancellation / Consulates</div><div class="cell tint"><svg class="mark"><use href="#tick"/></svg>Yes</div><div class="cell tint"><svg class="mark"><use href="#tick"/></svg>Yes</div><div class="cell tint">1</div>
  <div class="cell">Domestic Travel with Cremated Remains</div><div class="cell"><svg class="mark"><use href="#tick"/></svg>Yes</div><div class="cell"><svg class="mark"><use href="#cross"/></svg>No</div><div class="cell">1</div>
  <div class="cell tint">International Travel with Cremated Remains</div><div class="cell tint"><svg class="mark"><use href="#tick"/></svg>Yes</div><div class="cell tint"><svg class="mark"><use href="#tick"/></svg>Sometimes</div><div class="cell tint">1</div>
  <div class="cell">Domestic Forwarding of Remains</div><div class="cell"><svg class="mark"><use href="#tick"/></svg>Yes</div><div class="cell"><svg class="mark"><use href="#cross"/></svg>No</div><div class="cell">1</div>
  <div class="cell tint">International Forwarding of Remains</div><div class="cell tint"><svg class="mark"><use href="#tick"/></svg>Yes</div><div class="cell tint"><svg class="mark"><use href="#tick"/></svg>Yes</div><div class="cell tint">1</div>
  <div class="cell">Credit Cards / Utility Companies</div><div class="cell"><svg class="mark"><use href="#cross"/></svg>Usually Not</div><div class="cell"><svg class="mark"><use href="#cross"/></svg>No</div><div class="cell">0</div>
  <div class="cell tint">Personal Copy / Peace of Mind</div><div class="cell tint"><svg class="mark"><use href="#cross"/></svg>Optional</div><div class="cell tint"><svg class="mark"><use href="#cross"/></svg>Optional</div><div class="cell tint">1</div>
</div>

<div class="price-band">Pricing (Miami-Dade County):</div>

<p class="note" style="top:774px">The first certified death certificate is $20, and each additional copy is $16.</p>
<p class="note" style="top:814px">If you are traveling domestically or internationally with cremated remains, at least one certified copy is typically required. Some countries may require the certificate with cause of death. We will reach out to the consulate of the destination country to confirm the specific requirements for transporting cremated remains.</p>
<p class="note" style="top:895px">Please note: Other counties may have different pricing for death certificates. We will inform you of the exact cost based on the location of death.</p>
<p class="note" style="top:955px">Most families order 4 to 8 certified copies. A mix is common — for example, 2 with cause and 4 without cause. It simpler and more cost-effective to order them at the time of need. If you're unsure, we are here to guide you through the process.</p>

<section class="panel panel-order">
  <h2>How many certified copies would you like to order?</h2>
  <p><span class="box"></span>_ _ _ _ _ _ _ _ _ _With Cause of Death</p>
  <p><span class="box"></span>_ _ _ _ _ _ _ _ _ _Without Cause of Death</p>
</section>

<section class="panel panel-contact">
  <h2>Questions? We’re Here for You</h2>
  <p><svg class="ico" viewBox="0 0 12 12"><path d="M2.5 1 4.6 1.2 5.3 3.8 4 4.8C4.7 6.3 5.7 7.3 7.2 8L8.2 6.7 10.8 7.4 11 9.5C11 10.4 10.3 11 9.5 11 5 10.7 1.3 7 1 2.5 1 1.7 1.6 1 2.5 1Z" fill="#fff"/></svg>(305) 555-0148</p>
  <p><svg class="ico" viewBox="0 0 12 12"><rect x="0.5" y="2" width="11" height="8" rx="1" fill="#fff"/><path d="M1 2.8 6 6.5 11 2.8" fill="none" stroke="#cc9a16" stroke-width="1"/></svg><span>kendall@holliscrane.com | midtown@holliscrane.com | coralgables@holliscrane.com | preplanning@holliscrane.com</span></p>
</section>

<p class="closing">Serving Miami-Dade County with care, dignity, and support for over 100 years.</p>
</body>
</html>
```